Poster for Billard- & Sportsbar: "Specials"

Hi,
I Need a Poster for my Billard- & Sportsbar, which Shows our weekly Specials.
The size should be DinA0 (84 x 118.8 cm). Please notice the print instructions attached.

Text Information for the Poster:

"Wochenhighlights

Dienstag: Flatrate-Billard
Für nur 5€ (7€) pro Person den ganzen Abend Pool-Billard (Snooker)spielen

Mittwoch: Studenten-Nacht
Studenten & Auszubildende spielen Pool-Billard für nur 4,50€ die Stunde

Donnerstag: Snooker-Donnerstag
Donnerstags kostet der Snooker Tisch gerade mal 5€ die Stunde

Freitag: Kesselgold-Special
6 Talhof Kesselgold-Pils für nur 11,99€

Samstag: Schau dein Wunschsspiel
Reserviere die Private Lounge und schaue das Staffelrunde-Spiel deiner Wahl. Reservierungsgebühr: 10€, ab 6 Personen kostenlos.
(Gilt auch für EP, VKT-Pokal & Englische Wochen)

Sonntag: Play for Free
Wer vor 18:00 Uhr mit dem Spielen beginnt, spielt den ganzen Abend umsonst!"

You can choose the Colors free. If you use Pictures, take care that they are free or send me the link where they can get bought.

I have uploaded the logo of my bar. You can use it in the poster, but please not too big.

You can maybe use the Colors of the logo as main Colors. But it is not a must.

If you have questions, just contact me!

Thank you in advance!

Jorik

A short update: Please mind, that it is the most important Thing, that the customers can read the Special offers! Thank you

```html
<!DOCTYPE html>
<html lang="de">
<head>
<meta charset="utf-8">
<title>Wochenhighlights – Kugelhaus</title>
<link rel="stylesheet" href="https://fonts.googleapis.com/css2?family=Saira+Condensed:wght@500;600;700&display=swap">
<style>
  :root {
    --poster-black: #050505;
    --teal: #5fd3c6;
    --teal-soft: #6bb7a8;
    --frame-grey: #4a4a4a;
    --text-grey: #8c8c8c;
    --white: #ffffff;
    --felt-dark: #0c3b33;
    --felt: #14846c;
    --felt-light: #1c9c80;
  }
  html, body {
    margin: 0;
    padding: 0;
    width: 872px;
    height: 1200px;
    overflow: hidden;
    background: var(--poster-black);
  }
  .poster {
    position: relative;
    width: 872px;
    height: 1200px;
    background: var(--poster-black);
    font-family: "Saira Condensed", "Arial Narrow", sans-serif;
    overflow: hidden;
  }
  .table-photo {
    position: absolute;
    left: 0;
    top: 600px;
    width: 872px;
    height: 600px;
    background: linear-gradient(to bottom, var(--poster-black) 0%, var(--felt-dark) 18%, var(--felt) 50%, var(--felt-light) 100%);
  }
  .title {
    position: absolute;
    top: 30px;
    left: 0;
    width: 100%;
    margin: 0;
    text-align: center;
    color: var(--white);
    font-weight: 700;
    font-size: 56px;
    letter-spacing: 0.5px;
    line-height: 1;
  }
  .frames {
    position: absolute;
    left: 0;
    top: 0;
  }
  .column {
    position: absolute;
    top: 158px;
    width: 360px;
    text-align: center;
  }
  .column--left { left: 66px; }
  .column--right { left: 448px; }
  .special {
    position: absolute;
    left: 0;
    width: 100%;
    font-size: 19px;
    line-height: 24px;
    font-weight: 500;
    color: var(--text-grey);
  }
  .special p { margin: 0; }
  .special .day { color: var(--teal); font-weight: 600; }
  .special .name { color: var(--white); font-weight: 600; }
  .price { color: var(--teal); font-weight: 700; }
  .brand {
    position: absolute;
    top: 580px;
    left: 448px;
    width: 360px;
    text-align: center;
    color: #7d7d7d;
    font-weight: 700;
    font-size: 38px;
    letter-spacing: 1px;
    line-height: 1;
  }
  .address {
    position: absolute;
    left: 0;
    bottom: 36px;
    width: 100%;
    text-align: center;
    color: var(--teal-soft);
    font-weight: 600;
    font-size: 27px;
  }
</style>
</head>
<body>
<div class="poster">
  <div class="table-photo" role="img" aria-label="Photo of a green billiard table with racked coloured balls and a white cue ball in the foreground"></div>

  <h1 class="title">Wochenhighlights</h1>

  <svg class="frames" width="872" height="1200" viewBox="0 0 872 1200" aria-hidden="true">
    <rect x="60" y="120" width="368" height="556" rx="70" fill="none" stroke="var(--frame-grey)" stroke-width="2"/>
    <rect x="56" y="112" width="368" height="556" rx="70" fill="none" stroke="var(--teal)" stroke-width="2"/>
    <rect x="446" y="120" width="368" height="556" rx="70" fill="none" stroke="var(--frame-grey)" stroke-width="2"/>
    <rect x="442" y="112" width="368" height="556" rx="70" fill="none" stroke="var(--teal)" stroke-width="2"/>
  </svg>

  <div class="column column--left">
    <div class="special" style="top:0">
      <p class="day">Dienstag:</p>
      <p class="name">Flatrate-Billard</p>
      <p>Für nur <span class="price">5€ (7€)</span> pro Person den ganzen</p>
      <p>Abend Pool-Billard (Snooker)spielen</p>
    </div>
    <div class="special" style="top:136px">
      <p class="day">Donnerstag:</p>
      <p class="name">Snooker-Donnerstag</p>
      <p>Donnerstags kostet der Snooker</p>
      <p>Tisch gerade mal <span class="price">5€</span> die Stunde</p>
    </div>
    <div class="special" style="top:268px">
      <p class="day">Samstag:</p>
      <p class="name">Schau dein Wunschsspiel</p>
      <p>Reserviere die Private Lounge und</p>
      <p>schaue das Staffelrunde-Spiel deiner Wahl.</p>
      <p>Reservierungsgebühr: <span class="price">10€</span>, ab 6 Personen</p>
      <p>kostenlos. (Gilt auch für EP,</p>
      <p>VKT-Pokal &amp; Englische Wochen)</p>
    </div>
  </div>

  <div class="column column--right">
    <div class="special" style="top:0">
      <p class="day">Mittwoch:</p>
      <p class="name">Studenten-Nacht</p>
      <p>Studenten &amp; Auszubildende spielen</p>
      <p>Pool-Billard für nur <span class="price">4,50€</span> die Stunde</p>
    </div>
    <div class="special" style="top:130px">
      <p class="day">Freitag:</p>
      <p class="name">Kesselgold-Special 6</p>
      <p>Talhof Kesselgold-Pils für nur <span class="price">11,99€</span></p>
    </div>
    <div class="special" style="top:268px">
      <p class="day">Sonntag:</p>
      <p class="name">Play for Free</p>
      <p>Wer vor 18:00 Uhr mit dem Spielen</p>
      <p>beginnt, spielt den ganzen</p>
      <p>Abend umsonst!</p>
    </div>
  </div>

  <div class="brand">KUGELHAUS</div>

  <div class="address">Lindenweg 12, Talheim</div>
</div>
</body>
</html>
```